Stationery and Logo Design Project for new NZ Accounting Firm

Our company name is based in Auckland, New Zealand and is called TMV CA Limited. We are a chartered accountancy firm hence the CA abbreviations.

We need a full logo stationery design: Logo, Letterhead, Business Card and Compliments slip.

We are looking for a bold, modern and clean/simple design that makes us stand out. We want to stand out as professionals in the industry and would like the logo and stationery that our clients see to convey this image. We also want to break away from the traditional boring views of book/bean accountants. We are not doing the same old things others are doing and are mainly cloud based but with face to face business relationship focused as well.

We see ourselves as business advisers that provide more than just filing their tax returns. We want to add value to their business and be a partner in their business ventures.

We want the logo to convey the above and also attract potential clients when they see our ads among the thousands on zarvo and the tallow index.

The logo can be for the "TMV" with CA Ltd seperately or a logo/design beside the TMV. But open to other suggestions or concept.

Hi Designers

The designs I have received so far is not quite what I want.

I want something modern and bold that is DIFFERENT from others, from the usual logo designs. Some logo that when people look at it they will remember it as opposed to fading in the background of other competitors' logo.

Lower case lettering for the TMV could be something to explore as I have not seen a lot of these and they do appeal to me.

Thanks

We can focus on the logo first as that will form the main part for all stationery.

Reason: Final stages of choosing a logo design so need to time for designers to submit the letterhead, namecards designs.

Target Market(s)

Our target clients are small to medium business ranging from the sole trader to 50 employees businesses

Industry/Entity Type

Business

```html
<!DOCTYPE html>
<html lang="en">
<head>
<meta charset="utf-8">
<title>TMV CA Ltd — Stationery Set</title>
<link rel="stylesheet" href="https://fonts.googleapis.com/css2?family=Questrial&family=PT+Sans&display=swap">
<style>
  :root {
    --ink: #231f20;
    --slate-green: #4a6b63;
    --paper: #ffffff;
    --rule: #231f20;
    --brand-font: "Questrial", sans-serif;
    --body-font: "PT Sans", sans-serif;
  }
  * { box-sizing: border-box; margin: 0; padding: 0; }
  html, body { width: 1200px; height: 900px; overflow: hidden; background: var(--paper); }
  .canvas { position: relative; width: 1200px; height: 900px; background: var(--paper); }

  .wordmark {
    position: absolute;
    font-family: var(--brand-font);
    color: var(--ink);
    text-align: center;
    line-height: 1;
    background: var(--paper);
  }
  .wordmark span { display: block; }

  .logo-main { left: 137px; top: 150px; width: 253px; }
  .logo-main .name { font-size: 96px; }
  .logo-main .suffix { font-size: 30px; margin-top: 16px; }

  /* Letterhead */
  .letterhead {
    position: absolute; left: 577px; top: 57px; width: 556px; height: 787px;
    border: 1px solid var(--rule); background: var(--paper);
  }
  .letterhead .band { position: absolute; left: 42px; width: 476px; }
  .letterhead .band-heavy { top: 46px; height: 17px; background: var(--ink); }
  .letterhead .band-accent { top: 70px; height: 7px; background: var(--slate-green); }
  .letterhead .band-fine { top: 84px; height: 4px; background: var(--ink); }
  .letterhead .wordmark { left: 375px; top: 98px; width: 130px; padding: 6px 0; }
  .letterhead .name { font-size: 44px; }
  .letterhead .suffix { font-size: 15px; margin-top: 8px; }
  .contact-block {
    position: absolute; font-family: var(--brand-font); color: var(--ink);
    text-align: center; line-height: 1.25;
  }
  .letterhead .contact-block { left: 370px; top: 224px; width: 140px; font-size: 13px; }

  /* Compliments slip / envelope */
  .slip {
    position: absolute; left: 337px; top: 488px; width: 599px; height: 282px;
    border: 1px solid var(--rule); background: var(--paper);
  }
  .slip .frame {
    position: absolute; left: 24px; top: 21px; width: 549px; height: 238px;
    border: 1px solid var(--rule); border-radius: 10px; overflow: hidden;
  }
  .slip .band-heavy { position: absolute; left: 0; right: 0; top: 0; height: 17px; background: var(--ink); }
  .slip .band-accent { position: absolute; left: 0; right: 0; top: 23px; height: 7px; background: var(--slate-green); }
  .slip .band-fine { position: absolute; left: 0; right: 0; top: 37px; height: 2px; background: var(--ink); }
  .slip .wordmark { left: 438px; top: 45px; width: 122px; padding: 8px 0; }
  .slip .name { font-size: 46px; }
  .slip .suffix { font-size: 15px; margin-top: 10px; }
  .slip .contact-block { left: 429px; top: 191px; width: 140px; font-size: 14px; }

  /* Business card */
  .card {
    position: absolute; left: 50px; width: 248px; height: 155px;
    border: 1px solid var(--rule); border-radius: 10px; background: var(--paper); overflow: hidden;
  }
  .card-front { top: 472px; }
  .card-front .wordmark { left: 74px; top: 48px; width: 100px; }
  .card-front .name { font-size: 36px; }
  .card-front .suffix { font-size: 12px; margin-top: 8px; }
  .card-back { top: 634px; }
  .card-back .marker {
    position: absolute; left: 33px; top: 70px; width: 13px; height: 13px; background: var(--slate-green);
  }
  .card-back .panel {
    position: absolute; left: 53px; top: 19px; width: 196px; height: 115px;
    background: var(--ink); border-radius: 8px 0 0 8px;
  }
  .card-back .details {
    position: absolute; right: 33px; top: 30px; text-align: right;
    font-family: var(--body-font); font-size: 11px; line-height: 14px; color: var(--paper);
  }
</style>
</head>
<body>
<main class="canvas">
  <div class="wordmark logo-main"><span class="name">TMV</span><span class="suffix">CA Ltd</span></div>

  <section class="letterhead" aria-label="Letterhead">
    <div class="band band-heavy"></div>
    <div class="band band-accent"></div>
    <div class="band band-fine"></div>
    <div class="wordmark"><span class="name">TMV</span><span class="suffix">CA Ltd</span></div>
    <p class="contact-block">Address<br>Details<br>Contact Infos</p>
  </section>

  <section class="slip" aria-label="Compliments slip">
    <div class="frame">
      <div class="band-heavy"></div>
      <div class="band-accent"></div>
      <div class="band-fine"></div>
    </div>
    <div class="wordmark"><span class="name">TMV</span><span class="suffix">CA Ltd</span></div>
    <p class="contact-block">Address<br>Details<br>Contact Infos</p>
  </section>

  <section class="card card-front" aria-label="Business card front">
    <div class="wordmark"><span class="name">TMV</span><span class="suffix">CA Ltd</span></div>
  </section>

  <section class="card card-back" aria-label="Business card back">
    <div class="marker"></div>
    <div class="panel">
      <p class="details">Company Name<br>Details<br>Address<br>Contact</p>
    </div>
  </section>
</main>
</body>
</html>
```